Upscale business cards needed for family business

We need professional business cards created for several family members. We are a family business holding company. We would like these relatively simple and straightforward, but also with a unique element to set them apart. Probably stick with neutral and simple colors - white, grey etc. We need space for the traditional elements, including name, title, address, email/phone number. And we will be creating several from this template so it needs to be template that is easy to switch information in and out of.

Industry/Entity Type

Business

Contact Information for Business Card

Please include the attached Dunmore Ventures logo.

Requirements
Must have
• The attached Dunmore Ventures logo.

```html
<!DOCTYPE html>
<html lang="en">
<head>
<meta charset="utf-8">
<title>Dunmore Ventures – Business Card Spec</title>
<link rel="stylesheet" href="https://fonts.googleapis.com/css2?family=Mulish:wght@400;500&display=swap">
<style>
  :root {
    --paper: #ffffff;
    --ink: #111111;
    --matte-black: #090a09;
    --gold: #e9c62c;
    --gold-deep: #d6aa2a;
    --gold-light: #fdf7e2;
    --card-white: #f4f4f4;
    --callout: #e0309c;
    --note: #333333;
  }
  * { margin: 0; padding: 0; box-sizing: border-box; }
  html, body {
    width: 1200px;
    height: 1031px;
    overflow: hidden;
    background: var(--paper);
    font-family: "Mulish", "Helvetica Neue", Arial, sans-serif;
  }
  .spec-sheet { position: relative; width: 1200px; height: 1031px; }

  .callout-label {
    position: absolute;
    font-size: 17.5px;
    font-weight: 500;
    color: var(--ink);
    white-space: nowrap;
  }
  .callout-label--gold { left: 703px; top: 211px; }
  .callout-label--black { left: 328px; top: 681px; }
  .callout-line {
    position: absolute;
    width: 2px;
    background: var(--callout);
  }
  .callout-line--gold { left: 766px; top: 238px; height: 83px; }
  .callout-line--black { left: 374px; top: 589px; height: 83px; }

  .production-note {
    position: absolute;
    right: 333px;
    top: 648px;
    font-family: "Helvetica Neue", Arial, sans-serif;
    font-size: 16.5px;
    color: var(--note);
  }

  .business-card {
    position: absolute;
    left: 293px;
    top: 291px;
    width: 574px;
    height: 328px;
    overflow: hidden;
  }
  .card-background { position: absolute; inset: 0; display: block; }

  .company-name {
    position: absolute;
    left: 0; right: 0;
    top: 106px;
    text-align: center;
    font-size: 25px;
    font-weight: 500;
    letter-spacing: 1.5px;
    color: var(--card-white);
  }
  .holder-name {
    position: absolute;
    left: 0; right: 0;
    top: 170px;
    text-align: center;
    font-size: 25px;
    font-weight: 500;
    letter-spacing: 1px;
    color: var(--gold);
  }
  .holder-title {
    position: absolute;
    left: 0; right: 0;
    top: 201px;
    text-align: center;
    font-size: 17.5px;
    letter-spacing: 0.5px;
    color: var(--card-white);
  }
  .contact-line {
    position: absolute;
    left: 94px;
    font-size: 17.5px;
    letter-spacing: 0.6px;
    color: var(--card-white);
    white-space: nowrap;
  }
  .contact-line--address { top: 244px; }
  .contact-line--phone { top: 274px; }
  .contact-line--email { top: 274px; left: 260px; }
</style>
</head>
<body>
  <main class="spec-sheet">
    <span class="callout-label callout-label--gold">Metallic Gold</span>
    <span class="callout-line callout-line--gold"></span>

    <section class="business-card" aria-label="Dunmore Ventures business card front">
      <svg class="card-background" width="574" height="328" viewBox="0 0 574 328" aria-hidden="true">
        <defs>
          <linearGradient id="metallic-gold" x1="0" y1="0" x2="1" y2="0">
            <stop offset="0" stop-color="var(--gold)"/>
            <stop offset="0.12" stop-color="#eed354"/>
            <stop offset="0.33" stop-color="var(--gold-light)"/>
            <stop offset="0.5" stop-color="#efdc8a"/>
            <stop offset="0.68" stop-color="#e1c24a"/>
            <stop offset="0.87" stop-color="#ffffff"/>
            <stop offset="1" stop-color="var(--gold-deep)"/>
          </linearGradient>
        </defs>
        <rect class="gold-band" width="574" height="328" fill="url(#metallic-gold)"/>
        <path class="matte-panel" d="M0,107 C70,30 200,16 290,16 C400,16 520,40 574,98 L574,328 L0,328 Z" fill="var(--matte-black)"/>
      </svg>

      <div class="company-name">DUNMORE VENTURES</div>
      <div class="holder-name">DANIEL REYES</div>
      <div class="holder-title">CONSULTANT</div>
      <div class="contact-line contact-line--address">214 Marlowe Ave., Pasadena, CA 91105</div>
      <div class="contact-line contact-line--phone">626.555.0142</div>
      <div class="contact-line contact-line--email">d.reyes@dunmoreco.com</div>
    </section>

    <span class="production-note">(Name in metallic gold)</span>
    <span class="callout-line callout-line--black"></span>
    <span class="callout-label callout-label--black">Matte Black</span>
  </main>
</body>
</html>
```